Dunworthy Business Cards & Stationary
Rehabilitation Nurse Case Manager
Dunworthy Business Cards & Stationary - Medical
Creative Brief
Professional
Owen Dunworthy RN, CRRN, QRP
PO Box 812 Tarpon Springs, FL 34677-0812
owen@dunworthyandpartners.example
www.dunworthyandpartners.example
Please feel free to be creative. Would like design to be professional, innovative, and contemporary.
Large Logo with tagline, "Rehabilitation Nurse Case Manager" Also add bulleted listing of services we offer. These services are --Case Management -- Bill Review -- On-Site Analysis -- Home Safety Inspections

```html
<!DOCTYPE html>
<html lang="en">
<head>
<meta charset="utf-8">
<title>Dunworthy &amp; Associates – Business Card</title>
<link rel="stylesheet" href="https://fonts.googleapis.com/css2?family=Cinzel:wght@400;600;700&display=swap">
<style>
  :root{
    --bg:#ecebe8;
    --card:#ffffff;
    --navy:#0f1d5e;
    --navy-deep:#081447;
    --ink:#1c2a66;
    --white:#ffffff;
    --ghost:#dfe1ea;
  }
  *{margin:0;padding:0;box-sizing:border-box}
  html,body{width:1200px;height:971px;overflow:hidden;background:var(--bg)}
  .canvas{position:relative;width:1200px;height:971px}
  .card{position:absolute;width:573px;height:326px;border-radius:12px;overflow:hidden;background:var(--card);box-shadow:0 6px 18px rgba(0,0,0,.18)}
  .card-front{left:166px;top:153px;z-index:2}
  .card-back{left:479px;top:450px;z-index:1;background:linear-gradient(160deg,#ffffff 0%,#eef0f4 100%)}
  .card svg.bands{position:absolute;inset:0}
  .brand{position:absolute;font-family:"Cinzel",serif;color:var(--ink)}
  .brand-mark{position:absolute;left:86px;top:30px;width:92px;height:92px;border-radius:50%;background:var(--navy)}
  .brand-name{display:block;font-size:22px;font-weight:600;letter-spacing:.5px;line-height:1;white-space:nowrap}
  .brand-sub{display:flex;align-items:center;justify-content:center;gap:8px;font-size:9px;margin-top:5px;font-weight:600}
  .brand-sub::before,.brand-sub::after{content:"";width:34px;height:1px;background:var(--ink);opacity:.6}
  .card-front .brand{left:210px;top:38px}
  .contact{position:absolute;font-family:"Cinzel",serif;color:var(--white);font-size:10.5px;line-height:1.45;letter-spacing:.3px}
  .person{left:18px;top:222px;text-align:right;width:262px}
  .person .name{font-size:13px;font-weight:700;white-space:nowrap}
  .person .role{font-size:10.5px;font-weight:600;white-space:nowrap}
  .person .addr{margin-top:12px}
  .lines{left:305px;top:210px}
  .lines .web{margin-top:12px}
  .ghost-mark{position:absolute;left:18px;top:72px;width:218px;height:240px;border-radius:50%;background:var(--ghost);opacity:.75}
  .card-back .brand{right:36px;bottom:24px}
</style>
</head>
<body>
<main class="canvas">
  <section class="card card-front" aria-label="Business card front">
    <svg class="bands" width="573" height="326" viewBox="0 0 573 326" aria-hidden="true">
      <defs>
        <linearGradient id="silverBand" x1="0" y1="0" x2="1" y2="0">
          <stop offset="0" stop-color="#b7bac3"/>
          <stop offset=".5" stop-color="#e4e5ea"/>
          <stop offset="1" stop-color="#aeb2bc"/>
        </linearGradient>
        <linearGradient id="navyField" x1="0" y1="0" x2="0" y2="1">
          <stop offset="0" stop-color="#16257a"/>
          <stop offset="1" stop-color="#081447"/>
        </linearGradient>
      </defs>
      <path d="M0 150 C150 160 320 130 573 145 L573 326 L0 326 Z" fill="url(#silverBand)"/>
      <path d="M0 176 C180 180 330 152 573 170 L573 326 L0 326 Z" fill="url(#navyField)"/>
      <path d="M280 185 C380 170 470 168 573 176" stroke="#3f5bd0" stroke-width="1.5" fill="none" opacity=".7"/>
    </svg>
    <span class="brand-mark"></span>
    <div class="brand">
      <span class="brand-name">Dunworthy &amp; Associates</span>
      <span class="brand-sub">PLLC</span>
    </div>
    <div class="contact person">
      <div class="name">Owen Dunworthy RN, CRRN, QRP</div>
      <div class="role">Rehabilitation Nurse Case Manager</div>
      <div class="addr">PO Box 812<br>Cedar Bay, NC 34677-0812</div>
    </div>
    <div class="contact lines">
      <div>T: 877-555-0143</div>
      <div>P: 727-555-0178</div>
      <div>F: 727-555-0192</div>
      <div>E: owen@dunworthyandpartners.example</div>
      <div class="web">www.dunworthyandpartners.example</div>
    </div>
  </section>

  <section class="card card-back" aria-label="Business card back">
    <div class="ghost-mark"></div>
    <div class="brand">
      <span class="brand-name">Dunworthy &amp; Associates</span>
      <span class="brand-sub">PLLC</span>
    </div>
  </section>
</main>
</body>
</html>
```